PawHush business card

Looking for a fun and cool biz card for a new company with patent pending products. I have products to help and protect dogs hearing. My colors are pantone blue and orange.
Updates

Please add tag line: Protect the ones you love...even your PawHushes!

Target Market(s)

Animal/Dog lovers!

Industry/Entity Type

Retail

Contact Information for Business Card

I'm looking for something simple yet fun with all the info included for biz cards

Colors
0555a3
f78f20

Requirements
Must have
• Logo
Nice to have
• name, website and email
Should not have
• phone number

```html
<!DOCTYPE html>
<html lang="en">
<head>
<meta charset="utf-8">
<title>PawHush business card</title>
<link rel="stylesheet" href="https://fonts.googleapis.com/css2?family=Montserrat:wght@300;500;600;700&display=swap">
<style>
  :root {
    --stage: #4a4a4a;
    --card-blue: #2a3a8c;
    --card-blue-soft: #2f4096;
    --brand-orange: #f1592a;
    --white: #ffffff;
    --divider: rgba(255,255,255,0.75);
  }
  * { box-sizing: border-box; margin: 0; padding: 0; }
  html, body { width: 1200px; height: 1000px; overflow: hidden; }
  body {
    background: var(--stage);
    font-family: "Montserrat", sans-serif;
    position: relative;
  }
  .card {
    position: absolute;
    left: 210px;
    width: 780px;
    height: 450px;
    border-radius: 34px;
    background: var(--card-blue);
    overflow: hidden;
  }
  .card--front { top: 35px; }
  .card--back { top: 515px; }

  /* front */
  .front-brand {
    position: absolute;
    inset: 0;
    display: flex;
    align-items: center;
    justify-content: center;
    gap: 22px;
  }
  .brand-dot {
    width: 62px; height: 62px;
    border-radius: 50%;
    background: var(--brand-orange);
    flex: none;
  }
  .front-brand__name {
    font-weight: 700;
    font-size: 84px;
    color: var(--brand-orange);
    letter-spacing: -1px;
  }

  /* back */
  .back-brand {
    position: absolute;
    left: 60px;
    top: 205px;
    display: flex;
    align-items: center;
    gap: 14px;
  }
  .back-brand .brand-dot { width: 34px; height: 34px; }
  .back-brand__name {
    font-weight: 700;
    font-size: 58px;
    color: var(--brand-orange);
    letter-spacing: -1px;
    white-space: nowrap;
  }
  .back-divider {
    position: absolute;
    left: 405px;
    top: 40px;
    width: 1.5px;
    height: 290px;
    background: var(--divider);
  }
  .contact {
    position: absolute;
    left: 440px;
    top: 60px;
    width: 300px;
  }
  .contact__name {
    font-weight: 700;
    font-size: 27px;
    color: var(--white);
    white-space: nowrap;
  }
  .contact__title {
    font-weight: 300;
    font-size: 16px;
    color: var(--white);
    margin-top: 2px;
    margin-bottom: 22px;
    white-space: nowrap;
  }
  .contact__row {
    display: flex;
    align-items: center;
    gap: 8px;
    height: 36px;
    padding: 0 12px 0 8px;
    margin-bottom: 14px;
    border-radius: 6px;
    background: var(--brand-orange);
    color: var(--white);
    font-weight: 500;
    font-size: 18px;
    white-space: nowrap;
  }
  .contact__icon {
    width: 24px; height: 24px;
    flex: none;
    border-radius: 4px;
    background: var(--card-blue-soft);
    display: flex; align-items: center; justify-content: center;
  }
  .contact__row--step1 { margin-left: 0; }
  .contact__row--step2 { margin-left: 16px; }
  .back-rule {
    position: absolute;
    left: 60px;
    right: 40px;
    top: 370px;
    height: 2px;
    background: var(--white);
  }
  .back-address {
    position: absolute;
    left: 60px;
    top: 385px;
    font-weight: 600;
    font-size: 20px;
    color: var(--brand-orange);
    letter-spacing: 0.5px;
    white-space: nowrap;
  }
</style>
</head>
<body>
  <section class="card card--front" aria-label="Business card front">
    <div class="front-brand">
      <span class="brand-dot"></span>
      <span class="front-brand__name">PawHush</span>
    </div>
  </section>

  <section class="card card--back" aria-label="Business card back">
    <div class="back-brand">
      <span class="brand-dot"></span>
      <span class="back-brand__name">PawHush</span>
    </div>

    <div class="back-divider"></div>

    <div class="contact">
      <p class="contact__name">Dana Rowe</p>
      <p class="contact__title">Managing Director</p>
      <p class="contact__row contact__row--step1">
        <span class="contact__icon">
          <svg width="16" height="16" viewBox="0 0 16 16"><rect x="1.5" y="3.5" width="13" height="9" fill="none" stroke="#fff" stroke-width="1.5"/><path d="M1.5 3.5l6.5 5 6.5-5" fill="none" stroke="#fff" stroke-width="1.5"/></svg>
        </span>hello@pawhush.com
      </p>
      <p class="contact__row contact__row--step2">
        <span class="contact__icon">
          <svg width="16" height="16" viewBox="0 0 16 16"><circle cx="8" cy="8" r="6.2" fill="none" stroke="#fff" stroke-width="1.4"/><ellipse cx="8" cy="8" rx="2.6" ry="6.2" fill="none" stroke="#fff" stroke-width="1.2"/><path d="M2 8h12" stroke="#fff" stroke-width="1.2"/></svg>
        </span>www.pawhush.com
      </p>
    </div>

    <div class="back-rule"></div>
    <p class="back-address">01, PawHush building, your street, your country code - 12345</p>
  </section>
</body>
</html>
```